Pinecrest Valley Armory Banner

We are looking for a banner ad that we will run on DawnLedger.com the size is 758x120 and also a matching one that is 300x250 can be animated or static.final graphics will need to be submitted in jpg, gif or similar format. Our shop is a firearms business called "Pinecrest Valley Armory" located at 412 Route 19 South, Kosciusko Ms. 39417 phone is 662-574-3186 . it need to be modern and eye catching and be more geared to the tactical side. Our website is
pinecrestarmory.com the banners DO NOT have to match website. would like a DIFFERENT LOOK than my website

```html
<!DOCTYPE html>
<html lang="en">
<head>
<meta charset="utf-8">
<title>Pinecrest Valley Armory Banner</title>
<link rel="stylesheet" href="https://fonts.googleapis.com/css2?family=Bowlby+One+SC&family=Roboto+Condensed:wght@700&display=swap">
<style>
  :root {
    --bg-deep: #0d0e10;
    --bg-mid: #2c2f33;
    --steel: #5b5f64;
    --white: #ffffff;
    --ink: #000000;
    --call-blue: #1f4f9e;
    --call-blue-dark: #143a7a;
  }
  html, body {
    margin: 0;
    padding: 0;
    width: 1200px;
    height: 190px;
    overflow: hidden;
    background: var(--bg-deep);
  }
  .banner {
    position: relative;
    width: 1200px;
    height: 190px;
    overflow: hidden;
    font-family: "Roboto Condensed", Arial, sans-serif;
  }
  .banner__photo {
    position: absolute;
    inset: 0;
    background:
      radial-gradient(ellipse 420px 140px at 560px 110px, var(--steel) 0%, var(--bg-mid) 45%, transparent 80%),
      linear-gradient(90deg, var(--bg-deep) 0%, var(--bg-mid) 30%, #3a3d41 55%, var(--bg-mid) 75%, var(--bg-deep) 100%);
  }
  .brand {
    position: absolute;
    left: 10px;
    top: 10px;
    display: flex;
    align-items: center;
    gap: 14px;
  }
  .brand__mark {
    width: 66px;
    height: 66px;
    background: var(--steel);
    border: 3px solid var(--white);
    box-sizing: border-box;
  }
  .brand__name {
    margin: 0;
    color: var(--white);
    font-weight: 700;
    font-size: 27px;
    line-height: 1.1;
    width: 200px;
  }
  .headline {
    position: absolute;
    left: 370px;
    width: 520px;
    top: 22px;
    margin: 0;
    text-align: center;
    font-family: "Bowlby One SC", Impact, sans-serif;
    font-weight: 400;
    font-size: 46px;
    line-height: 64px;
    color: var(--white);
    letter-spacing: 1px;
    -webkit-text-stroke: 1.5px var(--ink);
    text-shadow: 3px 3px 0 var(--ink), -1px -1px 0 var(--ink);
  }
  .call {
    position: absolute;
    left: 926px;
    top: 27px;
    width: 264px;
    height: 84px;
    border-radius: 12px;
    background: linear-gradient(180deg, var(--call-blue) 0%, var(--call-blue-dark) 100%);
    display: flex;
    align-items: center;
    box-sizing: border-box;
    padding-left: 8px;
  }
  .call__icon {
    width: 66px;
    height: 66px;
    flex: none;
  }
  .call__text {
    flex: 1;
    text-align: center;
    color: var(--white);
    font-weight: 700;
    line-height: 1.35;
  }
  .call__label { font-size: 19px; display: block; }
  .call__number { font-size: 19px; display: block; }
</style>
</head>
<body>
  <div class="banner">
    <div class="banner__photo" role="img" aria-label="Close-up photograph of a dark steel semi-automatic pistol lying across the banner"></div>

    <div class="brand">
      <div class="brand__mark"></div>
      <p class="brand__name">Pinecrest Valley Armory</p>
    </div>

    <h1 class="headline">Firearms, Ammo<br>and Accessories</h1>

    <div class="call">
      <svg class="call__icon" viewBox="0 0 86 86" aria-hidden="true">
        <circle cx="43" cy="43" r="41" fill="#ffffff"/>
        <path d="M30 24c2-1 4-1 5 1l4 8c1 2 0 4-1 5l-3 2c2 5 6 9 11 11l2-3c1-1 3-2 5-1l8 4c2 1 2 3 1 5l-2 4c-2 3-5 4-8 3-13-4-23-14-27-27-1-3 0-6 3-8z" fill="#1f4f9e"/>
        <path d="M48 26a13 13 0 0 1 12 12M48 18a21 21 0 0 1 20 20" fill="none" stroke="#1f4f9e" stroke-width="3.5" stroke-linecap="round"/>
      </svg>
      <div class="call__text">
        <span class="call__label">Call Toll Free:</span>
        <span class="call__number">662-574-3186</span>
      </div>
    </div>
  </div>
</body>
</html>
```